Political Magazine & Corresponding Magazine Logo

I need a design for a monthly e-magazine that focuses on politics, public policy, as well as social, environmental, and economic justice. I would like a vibrant front and back cover, as well as internal pages that include a variety of design elements.

This magazine will be electronic ONLY and will not be published in print at this time.

I also need a logo design for the magazine that is attractive, includes the colors and images that communicate "authority" "trusted source", "professional", etc.

Industry/Entity Type

Political

Logo Text

Harborline Ember Review

Font styles to use
Serif
Sans Serif

Colors

Designer to choose colors to be used in the design.

Requirements
Must have
• I want the magazine design to include a variety of design elements that are consistent with the logo, as well as callouts, space for images, etc.
• I also need a logo design for the magazine that is attractive, includes the colors and images that communicate "authority" "trusted source", "professional", etc.
• I would like to have a color logo AND a white & black version of the same logo.
Nice to have
• I like various shades of navy blue.

```html
<!DOCTYPE html>
<html lang="en">
<head>
<meta charset="utf-8">
<title>Harborline Ember Review — Cover</title>
<link rel="stylesheet" href="https://fonts.googleapis.com/css2?family=Archivo:wght@400;700;800;900&family=Source+Serif+4:wght@400&display=swap">
<style>
  :root {
    --navy: #0a4a8c;
    --navy-deep: #0b3f78;
    --orange: #f39a1f;
    --paper: #f3f3f3;
    --white: #ffffff;
    --ink: #1d1d1d;
    --skin: #e9b8a4;
    --suit: #3d4a5c;
  }
  * { margin: 0; padding: 0; box-sizing: border-box; }
  html, body { width: 849px; height: 1200px; overflow: hidden; background: var(--paper); }
  .cover {
    position: relative; width: 849px; height: 1200px; overflow: hidden;
    background: var(--paper);
    font-family: "Archivo", Arial, sans-serif;
  }
  .cover-photo {
    position: absolute; inset: 0;
    background:
      radial-gradient(ellipse 260px 330px at 560px 560px, var(--skin) 0%, #d9a590 55%, rgba(217,165,144,0) 100%),
      radial-gradient(ellipse 200px 150px at 520px 760px, #6b5a50 0%, rgba(107,90,80,0) 100%),
      radial-gradient(ellipse 520px 300px at 450px 1180px, var(--suit) 0%, #56637a 50%, rgba(86,99,122,0) 100%),
      var(--paper);
  }
  .masthead { position: absolute; left: 0; top: 0; width: 849px; height: 360px; }
  .masthead text { font-family: "Archivo", Arial, sans-serif; font-weight: 900; fill: var(--navy); }
  .masthead .title-tag { fill: var(--white); font-weight: 800; }
  .issue-tag {
    position: absolute; left: 666px; top: 40px; width: 183px; height: 60px;
    background: var(--orange); color: var(--ink);
    padding: 9px 0 0 19px; font-size: 18px; line-height: 21px; letter-spacing: 1.5px;
  }
  .teaser-lead { position: absolute; left: 28px; top: 382px; width: 200px; }
  .teaser-lead h2 { color: var(--orange); font-weight: 800; font-size: 29px; line-height: 31px; }
  .teaser-lead p {
    margin-top: 10px; border-top: 1px dotted #999; border-bottom: 1px dotted #999;
    padding: 3px 0 5px; font-size: 13.5px; line-height: 18px; color: var(--ink);
  }
  .label { display: inline-block; font-weight: 700; font-size: 14px; line-height: 16px; padding: 1px 3px; margin-bottom: 4px; }
  .label-navy { background: var(--navy-deep); color: var(--white); }
  .label-orange { background: var(--orange); color: var(--white); font-size: 19px; line-height: 19px; margin-bottom: 2px; }
  .teaser-serif { position: absolute; left: 28px; top: 561px; width: 260px; }
  .teaser-serif h2 {
    font-family: "Source Serif 4", Georgia, serif; font-weight: 400;
    color: var(--navy); font-size: 35px; line-height: 36px; margin-top: 6px;
  }
  .teaser-plus { position: absolute; left: 33px; top: 764px; width: 240px; }
  .teaser-plus .plus-row { display: flex; gap: 14px; align-items: center; }
  .teaser-plus .labels { display: flex; flex-direction: column; align-items: flex-start; }
  .teaser-plus p { margin-top: 6px; color: var(--navy); font-size: 17px; line-height: 22px; }
  .stat-badge {
    position: absolute; left: 20px; top: 944px; width: 220px; height: 220px;
    border-radius: 50%; background: var(--navy); color: var(--white);
  }
  .stat-badge .figure { position: absolute; left: 32px; top: 18px; font-weight: 800; font-size: 104px; letter-spacing: -6px; line-height: 1; }
  .stat-badge .figure sup { font-size: 50px; vertical-align: top; position: relative; top: 6px; letter-spacing: 0; }
  .stat-badge .rule { position: absolute; left: 136px; top: 93px; width: 44px; height: 11px; background: var(--orange); }
  .stat-badge .caption {
    position: absolute; left: 40px; top: 128px; color: var(--orange);
    font-weight: 800; font-size: 16px; line-height: 19px; letter-spacing: -0.3px;
  }
  .headline-box {
    position: absolute; left: 322px; top: 954px; width: 527px; height: 130px;
    background: var(--white); padding: 6px 0 0 16px;
  }
  .headline-box h1 { font-weight: 800; font-size: 61px; line-height: 58px; letter-spacing: -2px; }
  .headline-box .line-navy { color: var(--navy); display: block; }
  .headline-box .line-orange { color: var(--orange); display: block; }
  .headline-dek { position: absolute; left: 322px; top: 1099px; width: 500px; font-size: 22px; line-height: 27px; }
  .headline-dek span { background: var(--navy-deep); color: var(--white); padding: 0 4px; box-decoration-break: clone; -webkit-box-decoration-break: clone; }
</style>
</head>
<body>
<main class="cover">
  <div class="cover-photo" role="img" aria-label="Cover portrait: a bald, bearded man in a dark suit and white shirt laughing, against a light studio background"></div>

  <svg class="masthead" viewBox="0 0 849 360" aria-label="Harborline Ember Review">
    <text x="36" y="144" font-size="150" textLength="570" lengthAdjust="spacingAndGlyphs">HARBORLINE</text>
    <text x="36" y="268" font-size="155" textLength="758" lengthAdjust="spacingAndGlyphs">EMBER</text>
    <rect x="32" y="272" width="368" height="75" fill="var(--orange)"/>
    <text class="title-tag" x="44" y="334" font-size="74" textLength="344" lengthAdjust="spacingAndGlyphs">REVIEW</text>
  </svg>

  <div class="issue-tag">VOLUME 1<br>2016 / 2017</div>

  <section class="teaser-lead">
    <h2>Voluptaatis atis tatistis atis tatis</h2>
    <p>Voluptatis vel pi ariatecis ariatem perunt inructorovit</p>
  </section>

  <section class="teaser-serif">
    <span class="label label-navy">VOLUPTATIS VEL</span><br>
    <span class="label label-navy">VOLUPTATIS</span>
    <h2>Voluptaatis vel iptptaatis vel iptatis</h2>
  </section>

  <section class="teaser-plus">
    <div class="plus-row">
      <svg width="40" height="40" viewBox="0 0 40 40" aria-hidden="true">
        <rect x="15" y="0" width="10" height="40" fill="var(--orange)"/>
        <rect x="0" y="15" width="40" height="10" fill="var(--orange)"/>
      </svg>
      <div class="labels">
        <span class="label label-orange">VOLUPTATIS</span>
        <span class="label label-orange">TATIS TATIS</span>
      </div>
    </div>
    <p>Voluptatis vel ipiciis e oluptatis vel ipiciis ent perunt inctorrovit</p>
  </section>

  <aside class="stat-badge">
    <div class="figure">10<sup>%</sup></div>
    <div class="rule"></div>
    <div class="caption">VOLUPTATIS VEL<br>IPICIIS ENT TATIS<br>VEL IPICIIS ENT</div>
  </aside>

  <section class="headline-box">
    <h1><span class="line-navy">Main Headline</span><span class="line-orange">Title here Head</span></h1>
  </section>
  <p class="headline-dek"><span>Voluptatis vel luptatis vel ipiciis vel oluptatis vel ipiciis vel uptatis ipiciis vel Voluptatis</span></p>
</main>
</body>
</html>
```